Business Card Design

Please copy the format of the attached card.

FRONT:
White text small blue horses head logo where "mirun" in in example

BACK:
Blue background w/ white horses head

Industry/Entity Type

Business

Contact Information for Business Card

Calvin Ostrow
Chief Executive Officer
Halvern Lodges & Resorts
412 Lindmoor Street | San Francisco, California 94109
Tel: +1.555.482.1937
email: calvin@halvernlodges.example

```html
<!DOCTYPE html>
<html lang="en">
<head>
<meta charset="utf-8">
<title>Halvern Lodges &amp; Resorts — Business Card</title>
<link rel="stylesheet" href="https://fonts.googleapis.com/css2?family=Arimo:wght@400;700&display=swap">
<style>
  :root {
    --backdrop: #d9dadc;
    --card-white: #f7f8f9;
    --brand-blue: #2f4f86;
    --ink-blue: #3d5f93;
    --back-blue: #1f5a7d;
    --back-blue-deep: #17465f;
    --white: #ffffff;
  }
  * { box-sizing: border-box; margin: 0; padding: 0; }
  html, body {
    width: 1200px; height: 1000px; overflow: hidden;
    background: var(--backdrop);
    font-family: "Arimo", Arial, sans-serif;
  }
  .canvas {
    position: relative; width: 1200px; height: 1000px;
    display: flex; flex-direction: column; align-items: center; justify-content: center; gap: 50px;
  }
  .card {
    position: relative; width: 700px; height: 400px;
    box-shadow: 0 10px 30px rgba(0,0,0,.18);
  }
  .card--front { background: var(--card-white); color: var(--ink-blue); }
  .rule {
    position: absolute; left: 0; right: 0; height: 0;
    border-top: 2px solid var(--brand-blue);
  }
  .rule--top { top: 36px; }
  .rule--bottom { bottom: 44px; }
  .contact {
    position: absolute; left: 52px; top: 60px;
    font-weight: 700; font-size: 15px; line-height: 23px;
  }
  .contact__line--email { font-weight: 400; }
  .identity { position: absolute; left: 52px; top: 160px; }
  .identity__name { font-size: 32px; font-weight: 400; color: var(--ink-blue); }
  .identity__title { font-size: 17px; font-weight: 700; margin-top: 6px; }
  .brand {
    position: absolute; display: flex; flex-direction: column; align-items: center; gap: 14px;
  }
  .card--front .brand { right: 48px; top: 150px; }
  .brand__dot { width: 74px; height: 74px; border-radius: 50%; background: var(--brand-blue); }
  .brand__name { font-size: 19px; font-weight: 700; color: var(--brand-blue); }
  .card--back {
    background: var(--back-blue);
    display: flex; align-items: center; justify-content: center;
  }
  .card--back .brand { position: static; }
  .card--back .brand__dot { width: 96px; height: 96px; background: var(--white); }
  .card--back .brand__name { color: var(--white); font-size: 22px; }
</style>
</head>
<body>
<main class="canvas">
  <section class="card card--front" aria-label="Card front">
    <div class="rule rule--top"></div>
    <div class="contact">
      <p class="contact__line">412 Lindmoor Street | San Francisco, California 94109</p>
      <p class="contact__line">Tel: +1.555.482.1937</p>
      <p class="contact__line contact__line--email">email: calvin@halvernlodges.example</p>
    </div>
    <div class="identity">
      <h1 class="identity__name">Calvin Ostrow</h1>
      <p class="identity__title">Chief Executive Officer</p>
    </div>
    <div class="brand">
      <span class="brand__dot"></span>
      <span class="brand__name">Halvern Lodges &amp; Resorts</span>
    </div>
    <div class="rule rule--bottom"></div>
  </section>
  <section class="card card--back" aria-label="Card back">
    <div class="brand">
      <span class="brand__dot"></span>
      <span class="brand__name">Halvern Lodges &amp; Resorts</span>
    </div>
  </section>
</main>
</body>
</html>
```